Bluestone Advisory & Mgmt - Professional Business Cards

Hi!

I am a Real Estate Developer and Construction Consultant.

I have a lot of inspiration from previous designs and would be open to using the attached Designs as a starting point. I would like to see these styles incorporated into your designs.

I really need professional business card to go with it that includes my important info.

Look forward to seeing your designs!.

Target Market(s)

My Target market are building owners, lawyers, consultants.

Industry/Entity Type

Real Estate Development

Contact Information for Business Card

My Name: Daniel Korvash
My Title: Principle
Company Name: Bluestone Advisory & Mgmt, LLC
Address: 348 West 41st Street, 7th FL New York, NY 10036
Mobile: 917.608.3719
Website: bam-hqx.com

Font styles to use
Serif
Sans Serif

Colors

Designer to choose colors to be used in the design.

Requirements
Must have
• Must incorporate the logo attached or have new that looks similar.
• Must use professional font that will be seen and judged by wealthy land owners and developers.
• Must incorporate some of the color green.
Should not have
• Photo's or pictures of people or buildings of any kind.

```html
<!DOCTYPE html>
<html lang="en">
<head>
<meta charset="utf-8">
<title>Bluestone Advisory &amp; Mgmt – Business Cards</title>
<link rel="stylesheet" href="https://fonts.googleapis.com/css2?family=Raleway:wght@400;500;700&family=Roboto:wght@400;500&display=swap">
<style>
  :root {
    --bg: #efefef;
    --card-white: #ffffff;
    --brand-green: #4cb87a;
    --text-green: #3fae6a;
    --ink: #2f2f2f;
    --muted: #8c8786;
    --divider: #555555;
  }
  * { margin: 0; padding: 0; box-sizing: border-box; }
  html, body {
    width: 1200px;
    height: 800px;
    overflow: hidden;
    background: var(--bg);
  }
  .canvas {
    position: relative;
    width: 1200px;
    height: 800px;
  }
  .card {
    position: absolute;
    width: 571px;
    height: 331px;
    box-shadow: 0 2px 6px rgba(0,0,0,0.12);
  }
  .card--front {
    left: 475px;
    top: 31px;
    background: var(--card-white);
  }
  .card--back {
    left: 170px;
    top: 405px;
    background: var(--brand-green);
  }

  /* Front: brand name block */
  .brand {
    position: absolute;
    left: 86px;
    top: 108px;
    width: 190px;
    display: flex;
    align-items: flex-start;
    gap: 10px;
    font-family: "Raleway", sans-serif;
    font-weight: 500;
    color: var(--text-green);
  }
  .brand__mark {
    flex: none;
    width: 14px;
    height: 14px;
    margin-top: 8px;
    background: var(--brand-green);
  }
  .brand__name {
    font-size: 24px;
    line-height: 1.2;
  }
  .brand__name small {
    display: block;
    font-size: 15px;
    line-height: 1.3;
    margin-top: 2px;
  }

  .divider {
    position: absolute;
    left: 287px;
    top: 104px;
    width: 2px;
    height: 113px;
    background: var(--divider);
  }

  .contact {
    position: absolute;
    left: 313px;
    top: 102px;
  }
  .contact__name {
    font-family: "Raleway", sans-serif;
    font-weight: 700;
    font-size: 17px;
    letter-spacing: 0.5px;
    color: var(--text-green);
  }
  .contact__title {
    font-family: "Raleway", sans-serif;
    font-weight: 700;
    font-size: 14px;
    color: var(--muted);
    margin-top: 2px;
  }
  .contact__list {
    list-style: none;
    margin-top: 14px;
    font-family: "Roboto", sans-serif;
    font-size: 16px;
    color: var(--ink);
  }
  .contact__list li {
    display: flex;
    align-items: center;
    gap: 6px;
    height: 22px;
  }
  .contact__list svg {
    width: 15px;
    height: 15px;
    flex: none;
    fill: var(--brand-green);
  }
  .accent { color: var(--text-green); }

  .company {
    position: absolute;
    left: 0;
    right: 0;
    top: 246px;
    text-align: center;
    font-family: "Roboto", sans-serif;
  }
  .company__legal {
    font-size: 15px;
    color: var(--text-green);
  }
  .company__address {
    font-size: 16px;
    color: var(--ink);
    margin-top: 7px;
  }

  /* Back */
  .brand--back {
    left: 354px;
    top: 182px;
    color: #ffffff;
  }
  .brand--back .brand__mark { background: #ffffff; }
</style>
</head>
<body>
<div class="canvas">

  <section class="card card--front">
    <div class="brand">
      <span class="brand__mark"></span>
      <div class="brand__name">Bluestone<small>Advisory Management</small></div>
    </div>

    <div class="divider"></div>

    <div class="contact">
      <div class="contact__name">DANIEL KORVASH</div>
      <div class="contact__title">Principle</div>
      <ul class="contact__list">
        <li>
          <svg viewBox="0 0 24 24" aria-hidden="true"><path d="M6.6 10.8a15.1 15.1 0 0 0 6.6 6.6l2.2-2.2a1 1 0 0 1 1-.25 11.4 11.4 0 0 0 3.6.57 1 1 0 0 1 1 1V20a1 1 0 0 1-1 1A17 17 0 0 1 3 4a1 1 0 0 1 1-1h3.5a1 1 0 0 1 1 1c0 1.25.2 2.45.57 3.57a1 1 0 0 1-.25 1z"/></svg>
          917.608.3719
        </li>
        <li>
          <svg viewBox="0 0 24 24" aria-hidden="true"><path d="M2 5h20v14H2z M2 5l10 7 10-7" fill="var(--brand-green)"/><path d="M2.5 5.5l9.5 6.7 9.5-6.7" fill="none" stroke="#fff" stroke-width="1.6"/></svg>
          info@bam-hqx.com
        </li>
        <li>
          <svg viewBox="0 0 24 24" aria-hidden="true"><circle cx="12" cy="12" r="10"/><path d="M7 7c2 0 3 1 3 3s2 2 2 4-1 3-1 5M15 5c0 2 1 3 3 3s2 2 2 3" fill="none" stroke="#fff" stroke-width="1.6"/></svg>
          <span>www.<span class="accent">bam-hqx</span>.com</span>
        </li>
      </ul>
    </div>

    <div class="company">
      <div class="company__legal">Bluestone Advisory &amp; Mgmt, LLC</div>
      <div class="company__address">348 West 41st Street, 7th FL New York, NY 10036</div>
    </div>
  </section>

  <section class="card card--back">
    <div class="brand brand--back">
      <span class="brand__mark"></span>
      <div class="brand__name">Bluestone<small>Advisory Management</small></div>
    </div>
  </section>

</div>
</body>
</html>
```